Give my personal webpage more appeal!

I need my CV website improved - drmeganholt.com.au.
I am using the template KESTREL from pagecraftly. i would like to keep the already existing theme but am open to suggestions.
Please focus on imagery, colour scheme, and textures to enhance the appeal and look of the page.
The content is there, but now I need a designer to improve the look of my page.
I need styling, royalty-free unique modern images to make the page professional, personal and friendly.
I work in healthcare, so I'm a people person.
I teach professionals and I treat a lot of families.

Target Market(s)

Parents, Professional Healthcare providers

Number of Pages Required

1 page

Font styles to use
Serif
Sans Serif

Requirements
Must have
• My face - image at the top, all the information already contained in it.
• Links to the websites I manage such as my blog.
• One Page website.
• All the information it already contains with the ability to have more.
• Ideally, we would keep the same format for the page although I'm happy to expand column and change the page's structure with in the theme template KESTREL.
Nice to have
• The current KESTREL template. I would like to keep the already existing theme but am open to suggestions.
Should not have
• Multiple pages.

```html
<!DOCTYPE html>
<html lang="en">
<head>
<meta charset="utf-8">
<title>Dr Megan Holt – Chiropractor – Skills</title>
<link href="https://fonts.googleapis.com/css2?family=Oswald:wght@300;400;600&family=Roboto:wght@300;400;500&display=swap" rel="stylesheet">
<style>
  :root {
    --amber: #efa717;
    --sidebar: #1e1512;
    --ink-light: #ffffff;
    --ink-soft: #e9e2dc;
    --ink-muted: #a9a39f;
    --nav-text: #d6d0cb;
  }
  * { box-sizing: border-box; margin: 0; padding: 0; }
  html, body { width: 1200px; height: 797px; overflow: hidden; }
  body { position: relative; font-family: "Roboto", sans-serif; background: var(--sidebar); }

  .sidebar {
    position: absolute; left: 0; top: 0; width: 385px; height: 797px;
    background: var(--sidebar);
  }
  .brand { position: absolute; left: 52px; top: 46px; width: 302px; }
  .brand-name {
    font-family: "Roboto", sans-serif; font-weight: 400; font-size: 40px;
    color: var(--amber); line-height: 1; letter-spacing: -0.5px;
  }
  .brand-tagline {
    display: flex; align-items: center; gap: 6px; margin-top: 14px;
    font-family: "Roboto", sans-serif; font-size: 13px; letter-spacing: 0.5px; color: var(--ink-muted);
  }
  .brand-tagline::before { content: ""; flex: 1; height: 3px; background: #8c8885; }

  .main-nav { position: absolute; left: 52px; top: 193px; width: 301px; list-style: none; }
  .main-nav li {
    height: 45px; display: flex; align-items: center; padding-left: 11px;
    font-family: "Oswald", sans-serif; font-weight: 300; font-size: 15px; color: var(--nav-text);
    border-bottom: 2px solid var(--amber);
  }
  .main-nav li.plain { border-bottom-color: transparent; }
  .main-nav li.active { background: var(--amber); color: #2a1d10; border-bottom-color: var(--amber); }

  .cv-button {
    position: absolute; left: 107px; top: 620px; width: 189px; height: 37px;
    border: 1px solid #8e8a87; display: flex; align-items: center; justify-content: center;
    font-family: "Oswald", sans-serif; font-weight: 400; font-size: 14px; color: #c9c4c0; letter-spacing: 0.3px;
  }
  .social { position: absolute; left: 126px; top: 690px; display: flex; gap: 8px; list-style: none; }
  .social li { width: 32px; height: 32px; border: 2px solid var(--amber); border-radius: 50%; }

  .contact { position: absolute; left: 0; width: 385px; top: 742px; text-align: center; font-size: 12px; color: var(--ink-light); line-height: 18px; }
  .contact span { color: var(--amber); }

  .hero {
    position: absolute; left: 385px; top: 0; width: 815px; height: 797px;
    background:
      radial-gradient(ellipse 260px 380px at 330px 620px, rgba(120,30,30,0.95), rgba(120,30,30,0) 100%),
      radial-gradient(ellipse 170px 200px at 330px 220px, rgba(95,55,45,0.9), rgba(95,55,45,0) 100%),
      radial-gradient(ellipse 300px 260px at 700px 120px, #6b7a35, rgba(107,122,53,0) 100%),
      linear-gradient(90deg, #3c4324 0%, #4a2a22 40%, #4a2a22 60%, #55612b 100%);
  }
  .hero-shade { position: absolute; left: 385px; top: 0; width: 815px; height: 797px; background: rgba(30,15,12,0.55); }

  .section-title {
    position: absolute; left: 428px; top: 63px;
    font-family: "Oswald", sans-serif; font-weight: 600; font-size: 25px; color: var(--ink-light);
  }
  .skill { position: absolute; width: 270px; }
  .skill h3 { font-weight: 500; font-size: 15px; color: var(--ink-light); height: 20px; line-height: 20px; }
  .skill p { font-weight: 300; font-size: 12px; line-height: 18px; color: var(--ink-soft); }
  .skill p + p { margin-top: 18px; }
  .skill .icon {
    position: absolute; width: 38px; height: 38px; border-radius: 50%; background: var(--amber);
    display: flex; align-items: center; justify-content: center;
  }
  .skill .icon svg { width: 20px; height: 20px; }

  .pager { position: absolute; left: 1152px; top: 318px; width: 26px; display: flex; flex-direction: column; align-items: center; }
  .pager-arrow { width: 26px; height: 26px; border: 1.5px solid #fff; border-radius: 50%; display: flex; align-items: center; justify-content: center; }
  .pager-dots { list-style: none; margin: 9px 0; }
  .pager-dots li { width: 9px; height: 9px; border-radius: 50%; background: var(--amber); margin: 6px 0; }
  .pager-dots li.current { background: #fff; }
</style>
</head>
<body>
  <aside class="sidebar">
    <div class="brand">
      <div class="brand-name">dr Megan Holt</div>
      <div class="brand-tagline">CHIROPRACTOR</div>
    </div>
    <ul class="main-nav">
      <li class="plain">About Me</li>
      <li class="active">Skills</li>
      <li>Professional Experiences</li>
      <li>Education</li>
      <li>Employment</li>
      <li>My Sites</li>
      <li>Blog</li>
      <li>Contact</li>
    </ul>
    <div class="cv-button">DOWNLOAD MY CV</div>
    <ul class="social" aria-label="Social profiles">
      <li></li><li></li><li></li><li></li>
    </ul>
    <div class="contact">
      Call me: <span>+61 0400 555 218</span><br>
      Email: <span>info@http://drmeganholt.com.au</span>
    </div>
  </aside>

  <div class="hero" role="img" aria-label="Portrait of Dr Megan Holt smiling in a red jacket, outdoors with green trees behind"></div>
  <div class="hero-shade"></div>

  <h2 class="section-title">SKILLS</h2>

  <section class="skill" style="left:473px; top:132px;">
    <h3>Business Development</h3>
    <div class="icon" style="left:-54px; top:42px;">
      <svg viewBox="0 0 20 20" fill="none" stroke="#fff" stroke-width="1.6"><path d="M2 17h16M3 15l4-6 3 3 4-6 3 5v4H3z" fill="#fff"/></svg>
    </div>
    <p style="margin-top:18px;">I founded an award winning Chiropractic healthcare clinic in 2005. It grew to employ five Chiropractors and eight support staff. Together we treated in excess of 18,000 patient appointments annually. I sold the business in 2016.</p>
    <p>2017 will see me roll out a new business strategy for a healthcare product entering the Australian market. This business will be in distribution, logistics and education of health professionals</p>
  </section>

  <section class="skill" style="left:475px; top:406px;">
    <h3>Teaching</h3>
    <div class="icon" style="left:-56px; top:45px;">
      <svg viewBox="0 0 20 20" fill="#fff"><path d="M10 2a1.5 1.5 0 0 1 1.5 1.5v.5A5 5 0 0 1 15 9v4l2 2H3l2-2V9a5 5 0 0 1 3.5-5v-.5A1.5 1.5 0 0 1 10 2zM8 16h4a2 2 0 0 1-4 0z"/></svg>
    </div>
    <p style="margin-top:16px;">I love the symbiotic relationship I have with my students. A room a-buzz with people eager to learn what I know, while I get a kick out of sharing what I know. The sharing of ideas and technique has taken me to the stage for community talks, healthcare industry seminars, as well as international congresses.</p>
  </section>

  <section class="skill" style="left:475px; top:601px;">
    <h3>Product launching</h3>
    <div class="icon" style="left:-56px; top:31px;">
      <svg viewBox="0 0 20 20" fill="#fff"><path d="M4 7h12l-1 10H5z"/><path d="M7 7V5a3 3 0 0 1 6 0v2" fill="none" stroke="#fff" stroke-width="1.6"/></svg>
    </div>
    <p style="margin-top:18px;">I have a special interest in product launching using the power of social media, connectedness with our natural network of colleagues and sensible targeted marketing strategies.</p>
  </section>

  <section class="skill" style="left:853px; top:132px;">
    <h3>Chiropractic Skills</h3>
    <div class="icon" style="left:-49px; top:42px;">
      <svg viewBox="0 0 20 20" fill="none" stroke="#fff" stroke-width="1.6"><circle cx="10" cy="10" r="7.5"/><circle cx="10" cy="10" r="4.5"/><circle cx="10" cy="10" r="1.6" fill="#fff"/></svg>
    </div>
    <p style="margin-top:18px;">Diagnostics using functional neurology and manual muscle testing along with manual Chiropractic adjusting skills has held me in good stead to influence the function and wellbeing of my patients since 2002. I see anyone with a body! From athletes at the top of their careers, sports people after their careers, active people, sedentary people, elderly people, middle aged people, and of course little people</p>
  </section>

  <section class="skill" style="left:853px; top:376px;">
    <h3>Mother &amp; Wife</h3>
    <div class="icon" style="left:-49px; top:41px;">
      <svg viewBox="0 0 20 20" fill="#fff"><path d="M10 17 3.5 10.5A3.8 3.8 0 0 1 10 5a3.8 3.8 0 0 1 6.5 5.5z"/></svg>
    </div>
    <p style="margin-top:18px;">I am a wife of a widower (WOM), a mother of two – one was a bonus, and one that I birthed. I have seen the seasons of life, the tidal flow, the ups and downs and the goodness that comes with positive thinking, gratefulness, persistence, hard work and a genuine interest and care for the people in our lives.</p>
  </section>

  <section class="skill" style="left:853px; top:582px;">
    <h3>Event Co-Ordination</h3>
    <div class="icon" style="left:-49px; top:41px;">
      <svg viewBox="0 0 20 20" fill="#fff"><path d="M3 3h14l-6 7v5h3v2H6v-2h3v-5z"/></svg>
    </div>
    <p style="margin-top:17px;">There's nothing quite like a deadline to get you focussed, and events are like a deadline that go off with a BANG! I love the build up and crescendo that event management brings to my life.</p>
  </section>

  <nav class="pager" aria-label="Section navigation">
    <div class="pager-arrow"><svg width="14" height="14" viewBox="0 0 14 14" fill="none" stroke="#fff" stroke-width="1.5"><path d="M2 9l5-5 5 5"/></svg></div>
    <ul class="pager-dots">
      <li class="current"></li><li></li><li></li><li></li><li></li><li></li><li></li>
    </ul>
    <div class="pager-arrow"><svg width="14" height="14" viewBox="0 0 14 14" fill="none" stroke="#fff" stroke-width="1.5"><path d="M2 5l5 5 5-5"/></svg></div>
  </nav>
</body>
</html>
```